Web Design for Financial Consulting Company

We need a website design for a financial consulting company "Kelvane Consulting". We build financial models, scenario analysis, handle the budgeting process and provide temporary staffing. I have over 10 years of experience. My Excel expertise and analytical savvy has saved clients over $17 million in profit.

Target Market(s)

Small to medium businesses

Industry/Entity Type

Financial Consulting

Number of Pages Required

4 page

Requirements
Must have
• Professional looking
Nice to have
• A little futuristic looking

```html
<!DOCTYPE html>
<html lang="en">
<head>
<meta charset="utf-8">
<title>Kelvane Consulting — Financial Consulting</title>
<link href="https://fonts.googleapis.com/css2?family=Epilogue:wght@300;400;500;600;700&display=swap" rel="stylesheet">
<style>
  :root {
    --accent: #00aeef;
    --accent-text: #1d9be0;
    --white: #ffffff;
    --ink: #0c0f13;
    --photo-dark: #1b1e22;
    --photo-mid: #3a3d40;
    --photo-light: #5d5f60;
    --overlay: rgba(10, 12, 15, 0.55);
  }
  * { margin: 0; padding: 0; box-sizing: border-box; }
  html, body {
    width: 1200px;
    height: 630px;
    overflow: hidden;
    background: var(--ink);
    font-family: "Epilogue", "Helvetica Neue", Arial, sans-serif;
    color: var(--white);
  }
  .page {
    position: relative;
    width: 1200px;
    height: 630px;
    overflow: hidden;
  }
  .hero-photo {
    position: absolute;
    inset: 0 0 36px 0;
    background:
      radial-gradient(ellipse 45% 55% at 70% 45%, var(--photo-light) 0%, transparent 70%),
      radial-gradient(ellipse 40% 45% at 25% 35%, var(--photo-mid) 0%, transparent 75%),
      linear-gradient(160deg, var(--photo-dark) 0%, var(--photo-mid) 55%, var(--photo-dark) 100%);
  }
  .hero-photo::after {
    content: "";
    position: absolute;
    inset: 0;
    background: var(--overlay);
  }
  .site-header {
    position: absolute;
    top: 28px;
    left: 88px;
    right: 88px;
    height: 42px;
    display: flex;
    align-items: center;
    justify-content: space-between;
  }
  .brand {
    display: flex;
    align-items: center;
    gap: 10px;
    text-decoration: none;
  }
  .brand-mark {
    width: 34px;
    height: 34px;
    border: 3px solid var(--accent);
  }
  .brand-name {
    font-size: 22px;
    font-weight: 600;
    letter-spacing: 1.5px;
    text-transform: uppercase;
    color: var(--white);
  }
  .main-nav {
    display: flex;
    align-items: center;
  }
  .main-nav a {
    color: var(--white);
    text-decoration: none;
    font-size: 14px;
    font-weight: 600;
    letter-spacing: 0.2px;
    margin-left: 37px;
  }
  .main-nav a.is-active {
    color: var(--accent-text);
    text-decoration: underline;
    text-underline-offset: 4px;
    margin-left: 0;
  }
  .btn-consult {
    display: inline-block;
    margin-left: 40px;
    padding: 10px 20px 9px;
    background: var(--accent);
    color: var(--white);
    font-size: 13.5px;
    font-weight: 700;
    text-decoration: none;
    text-transform: uppercase;
  }
  .hero-content {
    position: absolute;
    top: 232px;
    left: 0;
    right: 0;
    text-align: center;
  }
  .hero-title {
    font-size: 46px;
    line-height: 60px;
    font-weight: 300;
    text-transform: uppercase;
    letter-spacing: 0.3px;
  }
  .hero-title strong { font-weight: 700; }
  .btn-outline {
    display: inline-block;
    margin-top: 36px;
    width: 145px;
    height: 41px;
    line-height: 40px;
    border: 1.5px solid var(--accent);
    color: var(--accent-text);
    font-size: 13.5px;
    font-weight: 600;
    text-decoration: none;
    text-transform: uppercase;
  }
  .site-footer {
    position: absolute;
    left: 0;
    right: 0;
    bottom: 0;
    height: 36px;
    background: var(--accent);
    display: flex;
    align-items: center;
    justify-content: space-between;
    padding: 0 88px;
  }
  .copyright {
    font-size: 14px;
    font-weight: 400;
    color: var(--white);
  }
  .social-links {
    display: flex;
    gap: 9px;
  }
  .social-links a {
    display: block;
    width: 25px;
    height: 25px;
    border: 1px solid var(--white);
  }
  .social-links a.is-active { background: var(--white); }
</style>
</head>
<body>
  <div class="page">
    <div class="hero-photo" role="img" aria-label="Photo of consultants reviewing financial charts and reports at a desk"></div>

    <header class="site-header">
      <a class="brand" href="#">
        <span class="brand-mark"></span>
        <span class="brand-name">Kelvane Consulting</span>
      </a>
      <nav class="main-nav">
        <a class="is-active" href="#">Home</a>
        <a href="#">About Us</a>
        <a href="#">Services</a>
        <a href="#">Contact Us</a>
        <a class="btn-consult" href="#">Consult Now!</a>
      </nav>
    </header>

    <section class="hero-content">
      <h1 class="hero-title">We provide <strong>Financial</strong><br><strong>Consulting</strong> Service</h1>
      <a class="btn-outline" href="#">Get Started</a>
    </section>

    <footer class="site-footer">
      <p class="copyright">© 2023 Kelvane Consulting. All Right Reserved</p>
      <nav class="social-links" aria-label="Social links">
        <a href="#" aria-label="Social link 1"></a>
        <a class="is-active" href="#" aria-label="Social link 2"></a>
        <a href="#" aria-label="Social link 3"></a>
        <a href="#" aria-label="Social link 4"></a>
      </nav>
    </footer>
  </div>
</body>
</html>
```